Lumen Vale Consulting business card

I have a new logo that was designed for me here on CraftHive. I am a medical device marketing consultant. The medical device industry is very professional, kind of dry, and can be a bit boring. But I'm in marketing so I want to look fresh and innovative, within the confines of the industry.

Please use the logo to its potential, making it colorful and visually interesting (I know, there's really only one color. I need some kind of interesting design element - maybe wraparound...

Target Market(s)

Marketing management in medical device companies.

Industry/Entity Type

Marketing

Requirements
Must have
• Melissa Corbin
Phone: 949-555-0143
Address: Harbor Cove, CA
melissa@lumenvaleconsulting.example
www.lumenvaleconsulting.example

```html
<!DOCTYPE html>
<html lang="en">
<head>
<meta charset="utf-8">
<title>Lumen Vale Consulting – Business Card</title>
<link rel="stylesheet" href="https://fonts.googleapis.com/css2?family=Open+Sans:wght@400;600&display=swap">
<style>
  :root {
    --brand-blue: #2a9ad6;
    --ink-grey: #4a4d52;
    --soft-grey: #8a8d92;
    --rule-grey: #3c3f44;
    --card-white: #ffffff;
    --page-bg: #e9eaec;
  }
  html, body {
    margin: 0;
    padding: 0;
    width: 1200px;
    height: 1024px;
    overflow: hidden;
    background: var(--page-bg);
    font-family: "Open Sans", Arial, sans-serif;
  }
  .stage {
    position: relative;
    width: 1200px;
    height: 1024px;
  }
  .card {
    position: absolute;
    left: 270px;
    width: 660px;
    height: 377px;
    background: var(--card-white);
    box-shadow: 0 6px 18px rgba(0,0,0,0.15);
    box-sizing: border-box;
  }
  .card--front { top: 70px; }
  .card--back {
    top: 570px;
    background: linear-gradient(135deg, #ffffff 40%, #eeeff1 100%);
  }

  /* shared wordmark */
  .wordmark {
    display: flex;
    align-items: center;
    gap: 12px;
    color: var(--brand-blue);
    font-weight: 600;
    white-space: nowrap;
  }
  .wordmark__square {
    background: var(--brand-blue);
    flex: none;
  }

  /* front */
  .card--front .wordmark {
    position: absolute;
    left: 44px;
    top: 74px;
    font-size: 30px;
  }
  .card--front .wordmark__square { width: 22px; height: 22px; }
  .holder-name {
    position: absolute;
    right: 40px;
    top: 150px;
    margin: 0;
    font-size: 27px;
    font-weight: 600;
    color: var(--brand-blue);
  }
  .divider {
    position: absolute;
    left: 0;
    right: 0;
    top: 196px;
    height: 1px;
    background: var(--rule-grey);
  }
  .contact-list {
    position: absolute;
    left: 44px;
    top: 218px;
    margin: 0;
    padding: 0;
    list-style: none;
  }
  .contact-list li {
    display: flex;
    align-items: center;
    gap: 12px;
    font-size: 16px;
    color: var(--ink-grey);
    line-height: 34px;
  }
  .contact-list svg {
    width: 16px;
    height: 16px;
    flex: none;
  }

  /* back */
  .card--back .wordmark {
    position: absolute;
    left: 50%;
    top: 168px;
    transform: translateX(-50%);
    font-size: 40px;
  }
  .card--back .wordmark__square { width: 28px; height: 28px; }
  .site-line {
    position: absolute;
    left: 0;
    right: 0;
    top: 104px;
    margin: 0;
    text-align: center;
    font-size: 15px;
    letter-spacing: 4px;
    color: var(--ink-grey);
  }
  .site-line__domain { color: var(--brand-blue); }
</style>
</head>
<body>
<main class="stage">

  <section class="card card--front" aria-label="Business card front">
    <div class="wordmark"><span class="wordmark__square"></span>Lumen Vale Consulting</div>
    <h1 class="holder-name">Melissa Corbin</h1>
    <div class="divider"></div>
    <ul class="contact-list">
      <li>
        <svg viewBox="0 0 16 16" aria-hidden="true"><path d="M4 1.5c.6 0 1 .3 1.2.8l1 2.3c.2.5 0 1-.4 1.3l-1 .7c.8 1.7 2 2.9 3.6 3.7l.7-1c.3-.4.8-.6 1.3-.4l2.3 1c.5.2.8.7.8 1.2v1.6c0 .9-.7 1.6-1.6 1.5C6.6 13.7 2.3 9.4 1.9 3.1 1.8 2.2 2.5 1.5 3.4 1.5z" fill="var(--brand-blue)"/></svg>
        949-555-0143
      </li>
      <li>
        <svg viewBox="0 0 16 16" aria-hidden="true"><rect x="1" y="3" width="14" height="10" rx="1.5" fill="var(--brand-blue)"/><path d="M1.5 4l6.5 5 6.5-5" stroke="#fff" stroke-width="1.3" fill="none"/></svg>
        melissa@lumenvaleconsulting.example
      </li>
      <li>
        <svg viewBox="0 0 16 16" aria-hidden="true"><circle cx="8" cy="8" r="6.5" fill="none" stroke="var(--brand-blue)" stroke-width="1.4"/><ellipse cx="8" cy="8" rx="2.8" ry="6.5" fill="none" stroke="var(--brand-blue)" stroke-width="1.2"/><path d="M1.5 8h13M2.6 4.8h10.8M2.6 11.2h10.8" stroke="var(--brand-blue)" stroke-width="1.1"/></svg>
        www.lumenvaleconsulting.example
      </li>
      <li>
        <svg viewBox="0 0 16 16" aria-hidden="true"><path d="M8 1a5 5 0 0 1 5 5c0 3.6-5 9-5 9S3 9.6 3 6a5 5 0 0 1 5-5z" fill="var(--brand-blue)"/><circle cx="8" cy="6" r="1.8" fill="#fff"/></svg>
        Harbor Cove, CA
      </li>
    </ul>
  </section>

  <section class="card card--back" aria-label="Business card back">
    <p class="site-line">WWW.<span class="site-line__domain">LUMENVALECONSULTING</span>.EXAMPLE</p>
    <div class="wordmark"><span class="wordmark__square"></span>Lumen Vale Consulting</div>
  </section>

</main>
</body>
</html>
```